Business card design based on existing website

Please make a business card that is consistent with the look and feel of my new website: http://tellbury.com.sg. By going to the site, I think you'll have all you need in terms of the work I do and the colors I use.

I would like to ask the winner of this project to then do a separate project to design my stationery.

Target Market(s)

Heads of human resources, people wanting psychotherapy, and executives wanting coaching. (It's quite a mix!)

Industry/Entity Type

Psychology

Contact Information for Business Card

Email: ray5678@tellbury.com.sg
Website: http://tellbury.com.sg
Tel: +65 94706218

(I will not have a physical address on the card)

Font styles to use
Serif

Colors

Designer to choose colors to be used in the design.

Requirements
Must have
• On the Front
• ==========
• Have "Dr. Raymond Tellbury" using the font of the website.
• Also "Executive Coach, Psychotherapist, Leadership Professor"
• The back should mention
• ==================
• My degrees
• -------------
• "PhD Kelworth; Post Doc Drayfield". E.g., "Raymond Tellbury (PhD Kelworth; Post Doc Drayfield)" where the text between brackets was in smaller font.
• My work
• ----------
• "Executive coach, psychotherapist, and leadership professor"
• My job titles
• ---------------
• "Principal (Tellbury Consulting)
• Adjunct Professor (Lornvale Commerce University)
• Adjunct Associate Professor (Pemberly Institute of Letters)
• Coach & Supervisor (OKTRAV) '
• Options:
• 1) you can abbreviate Adjunct Professor to "Adj Prof" or "Adj Professor"; and "Adjunct Associate Professor" to "Adj Assoc Prof"
• 2) you abbreviate "Pemberly Institute of Letters" and "Lornvale Commerce University" to "PIL" and "LCU"
• 3) You can also combine the titles for PIL and LCU, e.g., "Adjunct faculty (PIL & LCU)
Nice to have
• Because I work with many Chinese people, it is sometimes helpful to have my family name, "Tellbury", in caps. In the past I have not used caps because it takes away from the aesthetic of the card. Only use caps if it looks good.
• The uploaded image of a "RT" is something that may be helpful. I am undecided.
• THANK YOU for helping me!
Should not have
• No photos. In my industry people consider it overselling.

```html
<!DOCTYPE html>
<html lang="en">
<head>
<meta charset="utf-8">
<title>Dr. Raymond Tellbury – Business Card</title>
<link rel="stylesheet" href="https://fonts.googleapis.com/css2?family=PT+Serif:wght@400&display=swap">
<style>
  :root {
    --forest: #285a14;
    --leaf: #4f7f3d;
    --sage: #9bb58f;
    --mist: #dfe8da;
    --paper: #ffffff;
    --paper-shade: #efefef;
    --name-green: #2f6412;
    --mark-green: #6c9561;
    --ink: #2e2e2e;
  }
  * { margin: 0; padding: 0; box-sizing: border-box; }
  html, body {
    width: 1200px;
    height: 720px;
    overflow: hidden;
    background: var(--paper);
  }
  .card {
    position: relative;
    width: 1200px;
    height: 720px;
    overflow: hidden;
    background:
      radial-gradient(ellipse at 100% 0%, var(--paper-shade) 0%, rgba(255,255,255,0) 55%),
      radial-gradient(ellipse at 100% 100%, var(--paper-shade) 0%, rgba(255,255,255,0) 50%),
      var(--paper);
  }
  .card__pattern {
    position: absolute;
    left: 0;
    top: 0;
    width: 600px;
    height: 720px;
    background: linear-gradient(90deg,
      var(--forest) 0%,
      #36691f 28%,
      var(--leaf) 42%,
      var(--sage) 60%,
      var(--mist) 78%,
      rgba(255,255,255,0) 100%);
  }
  .identity {
    position: absolute;
    right: 80px;
    top: 272px;
    text-align: right;
    font-family: "PT Serif", Georgia, serif;
  }
  .identity__mark {
    display: block;
    width: 34px;
    height: 34px;
    margin: 0 92px 10px auto;
    background: var(--mark-green);
  }
  .identity__name {
    font-size: 44px;
    font-weight: 400;
    line-height: 1;
    color: var(--name-green);
    letter-spacing: 0.2px;
    white-space: nowrap;
  }
  .identity__tagline {
    margin-top: 6px;
    font-size: 29px;
    font-weight: 400;
    line-height: 1.1;
    color: var(--ink);
    white-space: nowrap;
  }
</style>
</head>
<body>
  <main class="card">
    <div class="card__pattern" role="img" aria-label="Mosaic of green triangles fading from deep forest green at the left edge to white"></div>
    <section class="identity">
      <span class="identity__mark" aria-hidden="true"></span>
      <h1 class="identity__name">Dr. Raymond TELLBURY</h1>
      <p class="identity__tagline">Advancing Human Development</p>
    </section>
  </main>
</body>
</html>
```